Hopscotch Hattie needs updated Marketing Material!

Moving business to a new location and am looking to update all marketing material, including business cards, postcards, flyers, website. I've attached a copy of my current business card.
Updates

Good Morning!  I just received my new business phone number.  It is 724-305-9847

Hello All Designers!

Thank you for all the submissions I have received so far!  I wanted to give you a bit more background on what Hopscotch Hattie is all about:

I started this service when I was downsized out of a sales and marketing position.   A friend asked if I had time to run a few errands for her while she was at work.  "Lightbulb"!  I thought there must be more people that are over worked, over booked and want nothing more to do when they get home than spend time with their families or just relaxing.  And who wants to do all their running around on the weekends??  Hopscotch Hattie was born!

I have been extremely fortunate with my business here in California.  However, this summer I will be moving to a small town in Pennsylvania and I will be in uncharted territory.  I hope to have marketing material that will "WOW" all new potential clients.  Letting them know that I offer a unique service that can put time back into their week and free up their weekends for more important things.

If there is anything else I can tell you in order to help you with your design process, please let me know!
Thank you!
Hattie

Target Market(s)

Busy working parents and young professionals with disposable income that would like to spend their down time doing things that they enjoy rather than doing errands.

Industry/Entity Type

Marketing

```html
<!DOCTYPE html>
<html lang="en">
<head>
<meta charset="utf-8">
<title>Hopscotch Hattie – Business Card</title>
<link rel="stylesheet" href="https://fonts.googleapis.com/css2?family=Quicksand:wght@400;500;600&display=swap">
<style>
  :root {
    --stage: #505a5b;
    --lemon: #f2f51e;
    --lemon-soft: #e6ea3a;
    --olive-band: #c9c717;
    --royal: #1730f2;
    --royal-deep: #0f1fc4;
    --ink-blue: #1d2bb0;
    --paper: #ffffff;
    --text-dark: #333333;
    --bar-shadow: rgba(0,0,0,0.22);
  }
  * { box-sizing: border-box; margin: 0; padding: 0; }
  html, body { width: 1200px; height: 741px; overflow: hidden; }
  body {
    background: var(--stage);
    font-family: "Quicksand", sans-serif;
    position: relative;
  }
  .card {
    position: absolute;
    left: 399px;
    width: 409px;
    height: 237px;
    overflow: hidden;
  }
  .card--front { top: 89px; }
  .card--back { top: 413px; background: var(--paper); }

  /* Front */
  .front__top {
    position: absolute; inset: 0 0 auto 0; height: 76px;
    background: linear-gradient(90deg, var(--lemon) 0%, var(--lemon-soft) 100%);
  }
  .front__watermark-name {
    position: absolute; right: 12px; top: 14px;
    font-size: 17px; font-weight: 500;
    color: #d9d62a;
  }
  .front__body {
    position: absolute; left: 0; right: 0; top: 76px; height: 140px;
    background: linear-gradient(180deg, var(--royal) 0%, var(--royal-deep) 100%);
  }
  .front__bottom {
    position: absolute; left: 0; right: 0; bottom: 0; height: 21px;
    background: var(--olive-band);
    display: flex; align-items: center; justify-content: space-between;
    padding: 0 10px 0 4px;
    font-size: 13px; color: var(--ink-blue);
  }
  .contact { display: flex; align-items: center; gap: 5px; }
  .brand-name {
    position: absolute; left: 11px; top: 42px;
    font-size: 31px; font-weight: 400; color: var(--ink-blue);
    letter-spacing: 0.2px; white-space: nowrap;
  }
  .brand-tagline {
    position: absolute; left: 13px; top: 78px;
    font-size: 11.5px; font-weight: 500; color: var(--lemon);
  }
  .owner-name {
    position: absolute; left: 16px; top: 133px;
    font-size: 20px; font-weight: 500; color: var(--lemon);
  }
  .services {
    position: absolute; left: 225px; top: 109px;
    list-style: none;
    font-size: 10px; font-weight: 500; color: var(--lemon);
    line-height: 18px; white-space: nowrap;
  }

  /* Back */
  .side-bar {
    position: absolute; top: 72px; height: 144px;
    background: linear-gradient(180deg, var(--royal) 0%, var(--royal-deep) 100%);
    box-shadow: 0 0 6px var(--bar-shadow);
  }
  .side-bar--left { left: 0; width: 44px; }
  .side-bar--right { right: 0; width: 53px; }
  .back__brand {
    position: absolute; left: 44px; right: 53px; top: 98px;
    text-align: center;
    font-size: 22px; font-weight: 500; color: var(--ink-blue);
  }
  .back__tagline {
    position: absolute; left: 44px; right: 53px; top: 196px;
    text-align: center;
    font-size: 16px; font-weight: 400; color: var(--text-dark);
    word-spacing: 4px; white-space: nowrap;
  }
</style>
</head>
<body>
  <section class="card card--front">
    <div class="front__top">
      <span class="front__watermark-name" aria-hidden="true">Hopscotch Hattie</span>
    </div>
    <div class="front__body"></div>
    <h1 class="brand-name">Hopscotch Hattie</h1>
    <p class="brand-tagline">Personal Concierge and Errand Service</p>
    <p class="owner-name">Hattie Calloway</p>
    <ul class="services">
      <li>Personal shopping and Errands</li>
      <li>Household management</li>
      <li>Corporate concierge</li>
      <li>Project management</li>
      <li>Group rates for Teachers and seniors</li>
    </ul>
    <div class="front__bottom">
      <span class="contact">
        <svg width="11" height="8" viewBox="0 0 11 8" aria-hidden="true">
          <rect x="0.5" y="0.5" width="10" height="7" fill="none" stroke="#1d2bb0"/>
          <path d="M0.5 0.5 L5.5 4.5 L10.5 0.5" fill="none" stroke="#1d2bb0"/>
        </svg>
        hattie@hopscotchhattie.biz
      </span>
      <span class="contact">
        <svg width="7" height="12" viewBox="0 0 7 12" aria-hidden="true">
          <rect x="0.5" y="0.5" width="6" height="11" rx="1" fill="none" stroke="#1d2bb0"/>
          <rect x="1.5" y="2" width="4" height="4" fill="#1d2bb0"/>
        </svg>
        707.555.0148
      </span>
    </div>
  </section>

  <section class="card card--back">
    <div class="side-bar side-bar--left"></div>
    <div class="side-bar side-bar--right"></div>
    <p class="back__brand">Hopscotch Hattie</p>
    <p class="back__tagline">We hop to it so you don't have to!</p>
  </section>
</body>
</html>
```